Graphic Design for Vegas based contest

We are a bold, exciting, unique vacation designing company based in Las Vegas. We offer our busy clients Vegas vacation packages.

We want to appeal to young business professionals that want to make Vegas an experience to remember.

```html
<!DOCTYPE html>
<html lang="en">
<head>
<meta charset="utf-8">
<title>Vegas Unbound – Contest Poster</title>
<link rel="stylesheet" href="https://fonts.googleapis.com/css2?family=Almendra:wght@700&family=Poiret+One&display=swap">
<style>
  :root {
    --red-deep: #6e1210;
    --red-mid: #a3241f;
    --red-glow: #c23a31;
    --ink: #1a0807;
    --paper: #ffffff;
    --label: #f6d6d1;
    --silver-light: #f2f2f2;
    --silver-dark: #9a9a9a;
    --badge-red: #8c1d19;
  }
  html, body {
    margin: 0;
    padding: 0;
    overflow: hidden;
    background: #ffffff;
  }
  .poster {
    position: relative;
    width: 883px;
    height: 1200px;
    overflow: hidden;
    background:
      radial-gradient(ellipse 70% 55% at 55% 45%, var(--red-glow) 0%, var(--red-mid) 45%, var(--red-deep) 100%);
    font-family: "Poiret One", sans-serif;
  }
  .brand-name {
    position: absolute;
    top: 118px;
    left: 0;
    width: 100%;
    margin: 0;
    text-align: center;
    font-family: "Almendra", serif;
    font-weight: 700;
    font-size: 108px;
    line-height: 1;
    color: var(--silver-light);
  }
  .city-illustration {
    position: absolute;
    left: 50px;
    top: 345px;
    width: 680px;
    height: 500px;
    border-radius: 46% 52% 40% 48%;
    background: radial-gradient(ellipse at 50% 45%, #f4f4f4 0%, #cfcfcf 55%, #8e8e8e 100%);
  }
  .prize-badge {
    position: absolute;
    left: 490px;
    top: 470px;
    width: 280px;
    height: 280px;
  }
  .prize-badge svg { display: block; }
  .prize-badge-text {
    position: absolute;
    inset: 0;
    display: flex;
    flex-direction: column;
    align-items: center;
    justify-content: center;
    color: var(--paper);
    text-align: center;
    line-height: 1;
  }
  .prize-win { font-size: 82px; letter-spacing: 2px; }
  .prize-tour { font-size: 34px; margin-top: 2px; }
  .prize-place { font-size: 21px; margin-top: 6px; line-height: 1.05; }
  .question-tag {
    position: absolute;
    left: 30px;
    top: 780px;
    width: 210px;
    height: 50px;
    background: var(--paper);
    border-radius: 10px 26px 26px 10px;
    display: flex;
    align-items: center;
    justify-content: center;
    font-size: 38px;
    color: var(--ink);
  }
  .question-headline {
    position: absolute;
    top: 842px;
    left: 0;
    width: 100%;
    margin: 0;
    text-align: center;
    font-family: "Almendra", serif;
    font-weight: 700;
    font-size: 56px;
    line-height: 64px;
    color: var(--ink);
  }
  .question-headline .line-light { color: var(--paper); }
  .instructions {
    position: absolute;
    left: 30px;
    right: 28px;
    top: 990px;
    color: var(--paper);
    font-size: 26px;
    line-height: 32px;
  }
  .instructions p { margin: 0 0 20px; }
  .instructions .label { color: var(--label); font-weight: 400; }
</style>
</head>
<body>
<main class="poster">
  <h1 class="brand-name">Vegas Unbound</h1>

  <div class="city-illustration" role="img" aria-label="Black and white line illustration of a burst of Las Vegas city elements: towers, traffic light, double-decker bus, arrows and stars"></div>

  <div class="prize-badge">
    <svg width="280" height="280" viewBox="0 0 100 100" aria-hidden="true">
      <defs>
        <linearGradient id="silverRim" x1="0" y1="0" x2="1" y2="1">
          <stop offset="0" stop-color="#f2f2f2"/>
          <stop offset="1" stop-color="#9a9a9a"/>
        </linearGradient>
      </defs>
      <polygon fill="url(#silverRim)" points="50,0 58,13 72,5 73,21 89,19 83,34 98,41 86,51 97,63 81,67 85,83 69,80 63,96 52,85 40,97 35,81 18,85 21,69 4,64 15,52 3,40 19,35 13,20 29,21 31,5 44,14"/>
      <polygon fill="#8c1d19" points="50,7 57,18 69,11 69,25 83,24 78,37 91,43 80,51 90,61 76,64 79,78 66,75 60,89 51,79 41,89 37,75 22,78 25,65 11,61 20,51 10,43 23,38 18,25 32,25 33,11 45,19"/>
    </svg>
    <div class="prize-badge-text">
      <span class="prize-win">WIN</span>
      <span class="prize-tour">a tour</span>
      <span class="prize-place">zion national<br>park</span>
    </div>
  </div>

  <div class="question-tag">question</div>

  <h2 class="question-headline">
    What are the 7 Natural<br>
    <span class="line-light">Wonders of the World?</span>
  </h2>

  <section class="instructions">
    <p><span class="label">brief instructions:</span> enter to win a tour of zion national park for 2 provided by wayfare nv</p>
    <p><span class="label">detailed instructions:</span> list the seven natural wonders of the world and be entered to win a tour of zion national park for 2 provided by wayfare nv</p>
  </section>
</main>
</body>
</html>
```